Stylish business cards for KX7

To create an appealing and professional business card design for a WOMEN Owned Construction Supply Company.
2 sided card. Incorporate brand elements, curvy, colorful, sleek and bright. No solid white background. attached samples of styles added shapes/ribbons. Want something with that WOW that looks awesome, factor. It is a new logo, so feel free to mess with logo colors in the blue and teal factors that can look good with both dark and light background. If you want to try a watermark with just the KX7, without the "Supply" that might look cool to.

Industry/Entity Type

Women owned construction supply company

Contact Information for Business Card

Name, Title, and phone number and email, web page. maybe spot for qr code.

Font styles to use
Sans Serif

Requirements
Nice to have
• would love to see colors, maybe stylish ribbon dividers or some sort of 2 or 3 tone color card that compliments logo.
Should not have
• Please do not have all white background. Do not include Home/reale state/ or building images.

```html
<!DOCTYPE html>
<html lang="en">
<head>
<meta charset="UTF-8">
<title>KX7 Supply Business Card</title>
<link rel="stylesheet" href="https://fonts.googleapis.com/css2?family=Roboto:wght@400;500&display=swap">
<style>
  :root {
    --stage: #777777;
    --card: #ffffff;
    --card-tint: #e8f2f7;
    --navy: #1b3d60;
    --navy-mid: #245a7c;
    --teal: #2190b5;
    --ink-light: #ffffff;
    --ink-soft: #cfe4ef;
  }
  * { margin: 0; padding: 0; box-sizing: border-box; }
  html, body {
    width: 1199px; height: 1200px; overflow: hidden;
    background: var(--stage);
    font-family: "Roboto", sans-serif;
  }
  .canvas { position: relative; width: 1199px; height: 1200px; }
  .card {
    position: absolute; left: 172px; width: 855px; height: 500px;
    background: var(--card); overflow: hidden;
  }
  .card-front { top: 81px; }
  .card-back {
    top: 618px;
    background: linear-gradient(135deg, var(--card) 0%, var(--card-tint) 100%);
  }
  .card-art { position: absolute; inset: 0; width: 100%; height: 100%; }

  .holder-name {
    position: absolute; left: 62px; top: 236px;
    font-size: 33px; font-weight: 500; color: var(--ink-light); line-height: 1.1;
  }
  .holder-title {
    position: absolute; left: 64px; top: 282px;
    font-size: 19px; font-weight: 400; color: var(--ink-soft); letter-spacing: 0.5px;
  }
  .contact-line {
    position: absolute; display: flex; align-items: center; gap: 10px;
    font-size: 21px; font-weight: 400; line-height: 1; color: var(--ink-light);
  }
  .contact-line svg { width: 18px; height: 18px; flex: none; }
  .contact-phone { left: 64px; top: 336px; }
  .contact-email { left: 64px; top: 369px; }
  .contact-web { left: 64px; top: 402px; }
  .contact-address {
    position: absolute; left: 508px; top: 363px;
    display: flex; gap: 10px; color: var(--navy);
    font-size: 21px; line-height: 33px;
  }
  .contact-address svg { width: 20px; height: 24px; margin-top: 4px; flex: none; }

  .brand-name {
    position: absolute; color: var(--navy); font-weight: 500;
    white-space: nowrap; transform: translate(-50%, -50%);
  }
  .card-front .brand-name { left: 610px; top: 240px; font-size: 46px; }
  .card-back .brand-name { left: 427px; top: 240px; font-size: 66px; }
</style>
</head>
<body>
<div class="canvas">

  <section class="card card-front">
    <svg class="card-art" viewBox="0 0 684 400" preserveAspectRatio="none" aria-hidden="true">
      <defs>
        <linearGradient id="navyPanel" x1="0" y1="0" x2="1" y2="0">
          <stop offset="0" stop-color="#1b3d60"/>
          <stop offset="1" stop-color="#245a7c"/>
        </linearGradient>
        <linearGradient id="baseRibbon" x1="0" y1="0" x2="1" y2="0">
          <stop offset="0" stop-color="#1b3d60"/>
          <stop offset="0.5" stop-color="#235a7a"/>
          <stop offset="1" stop-color="#2190b5"/>
        </linearGradient>
        <linearGradient id="tealRibbon" x1="0" y1="0" x2="1" y2="1">
          <stop offset="0" stop-color="#2a9cc0"/>
          <stop offset="1" stop-color="#1d7fa5"/>
        </linearGradient>
        <filter id="soft" x="-20%" y="-20%" width="140%" height="140%">
          <feGaussianBlur stdDeviation="6"/>
        </filter>
      </defs>
      <polygon points="214,0 378,370 684,370 684,378 372,378" fill="#000" opacity="0.18" filter="url(#soft)"/>
      <polygon points="0,0 207,0 367,365 0,365" fill="url(#tealRibbon)"/>
      <polygon points="0,0 10,8 367,365 0,365" fill="#000" opacity="0.2" filter="url(#soft)"/>
      <polygon points="0,0 367,365 0,365" fill="url(#navyPanel)"/>
      <rect x="0" y="365" width="684" height="35" fill="url(#baseRibbon)"/>
    </svg>

    <div class="brand-name">KX7 Supply</div>

    <h1 class="holder-name">Dana Reyes</h1>
    <p class="holder-title">Owner &amp; Founder</p>
    <div class="contact-line contact-phone">
      <svg viewBox="0 0 20 20"><circle cx="10" cy="10" r="10" fill="#fff"/><path d="M7 5.5l1.6 2.4-1 1.1a7 7 0 0 0 3.4 3.4l1.1-1 2.4 1.6-.8 1.6c-3.7-.2-7.5-4-7.7-7.7z" fill="#1f4a6c"/></svg>
      <span>555-0142-7788</span>
    </div>
    <div class="contact-line contact-email">
      <svg viewBox="0 0 20 20"><circle cx="10" cy="10" r="10" fill="#fff"/><rect x="5" y="6.5" width="10" height="7" rx="1" fill="#22506f"/><path d="M5.5 7.2L10 10.5l4.5-3.3" stroke="#fff" stroke-width="1" fill="none"/></svg>
      <span>info@kx7supply.com</span>
    </div>
    <div class="contact-line contact-web">
      <svg viewBox="0 0 20 20"><circle cx="10" cy="10" r="10" fill="#fff"/><circle cx="10" cy="10" r="5.5" fill="none" stroke="#22506f" stroke-width="1.3"/><path d="M4.5 10h11M10 4.5c-2.5 3-2.5 8 0 11M10 4.5c2.5 3 2.5 8 0 11" fill="none" stroke="#22506f" stroke-width="1.1"/></svg>
      <span>www.kx7supply.com</span>
    </div>
    <div class="contact-address">
      <svg viewBox="0 0 20 24"><path d="M10 0a9 9 0 0 1 9 9c0 6-9 15-9 15S1 15 1 9a9 9 0 0 1 9-9z" fill="#2190b5"/><circle cx="10" cy="9" r="3.5" fill="#fff"/></svg>
      <address style="font-style:normal">41 Harbor Lane,<br>Zip-204518</address>
    </div>
  </section>

  <section class="card card-back">
    <svg class="card-art" viewBox="0 0 684 400" preserveAspectRatio="none" aria-hidden="true">
      <defs>
        <linearGradient id="backRibbon" x1="0" y1="0" x2="1" y2="0">
          <stop offset="0" stop-color="#1b3d60"/>
          <stop offset="0.5" stop-color="#235a7a"/>
          <stop offset="1" stop-color="#2190b5"/>
        </linearGradient>
        <linearGradient id="backTeal" x1="0" y1="0" x2="1" y2="0">
          <stop offset="0" stop-color="#2190b5"/>
          <stop offset="1" stop-color="#2a9cc0"/>
        </linearGradient>
        <filter id="softBack" x="-20%" y="-20%" width="140%" height="140%">
          <feGaussianBlur stdDeviation="5"/>
        </filter>
      </defs>
      <polygon points="420,400 684,300 684,400" fill="#000" opacity="0.15" filter="url(#softBack)"/>
      <polygon points="440,400 684,310 684,400" fill="url(#backTeal)"/>
      <rect x="0" y="365" width="684" height="35" fill="url(#backRibbon)"/>
    </svg>
    <div class="brand-name">KX7 Supply</div>
  </section>

</div>
</body>
</html>
```